One on one Pilates studio needs business card design

I need a business card design for my Pilates studio in Lakeland FL. It is a one-on-one studio, which is located on our property where we also have a U-Pick blueberry farm. I would like the back to have a place for appointment times/dates (I work Mon-Sat). Quote to use by Conrad Vellmer--"Physical fitness can neither be achieved by wishful thinking nor outright purchased". I don't just want a white card with my logo and info please. A natural material look

Target Market(s)

Fitness/ Pilates

Industry/Entity Type

Business

Contact Information for Business Card

Like raised wording, natural look

Colors
55b5dd
3176b5
acd036
cadf82

Requirements
Must have
• Back side for appointment setting. Conrad Vellmer quote. Owner, Pilates instructor. One-on-one studio.

```html
<!DOCTYPE html>
<html lang="en">
<head>
<meta charset="utf-8">
<title>Orchard Row – Business Card, Back and Front</title>
<link rel="stylesheet" href="https://fonts.googleapis.com/css2?family=Lato:wght@400;700;900&family=Lora:ital,wght@1,400&display=swap">
<style>
  :root {
    --page-bg: #e9ecef;
    --card-bg: #fbfbfb;
    --sky: #55b5dd;
    --ocean: #3176b5;
    --accent-blue: #3ea1d2;
    --leaf: #acd036;
    --leaf-deep: #93bb22;
    --text-gray: #666a6e;
    --ink: #3f4245;
    --divider-dark: #6d6f72;
    --divider-light: #e2e3e4;
  }
  * { box-sizing: border-box; margin: 0; padding: 0; }
  html, body { width: 1200px; height: 900px; overflow: hidden; }
  body {
    background: var(--page-bg);
    font-family: "Lato", Arial, sans-serif;
    position: relative;
  }
  .card {
    position: absolute;
    left: 240px;
    width: 720px; height: 412px;
    background: var(--card-bg);
    box-shadow: 0 8px 24px rgba(0,0,0,.16);
    overflow: hidden;
  }
  .card-back { top: 26px; }
  .card-front { top: 462px; }
  .card-bands { position: absolute; inset: 0; width: 100%; height: 100%; }

  /* Back side */
  .quote {
    position: absolute; left: 50px; top: 52px; width: 620px;
    font-family: "Lora", Georgia, serif; font-style: italic;
    font-size: 25px; line-height: 1.35; color: var(--accent-blue);
  }
  .quote-author {
    position: absolute; right: 50px; top: 128px;
    font-weight: 700; font-size: 15px; color: var(--text-gray);
  }
  .day-picker {
    position: absolute; left: 50px; top: 190px; width: 620px;
    display: flex; justify-content: space-between; list-style: none;
  }
  .day-picker li {
    display: flex; align-items: center; gap: 8px;
    font-weight: 900; font-size: 19px; color: var(--accent-blue);
  }
  .check-box {
    width: 26px; height: 26px; border: 3px solid var(--ink); border-radius: 5px;
  }
  .slot-row {
    position: absolute; left: 50px; top: 268px; width: 620px;
    display: flex; align-items: flex-end; gap: 14px;
    font-weight: 900; font-size: 19px; color: var(--accent-blue);
  }
  .slot-line { flex: 1; border-bottom: 2px solid var(--ink); height: 22px; }
  .slot-line.short { flex: 0.8; }
  .meridiem { display: flex; gap: 14px; }

  /* Front side */
  .brand {
    position: absolute; left: 56px; top: 176px;
    display: flex; align-items: center; gap: 12px;
  }
  .brand-dot { width: 34px; height: 34px; border-radius: 50%; background: var(--accent-blue); }
  .brand-name { font-weight: 700; font-size: 44px; color: var(--leaf-deep); }
  .divider {
    position: absolute; left: 398px; top: 70px;
    width: 4px; height: 292px;
    background: linear-gradient(to bottom, var(--divider-light), var(--divider-dark));
  }
  .contact { position: absolute; left: 432px; top: 52px; }
  .holder-name { font-weight: 900; font-size: 24px; color: var(--accent-blue); }
  .holder-role { font-weight: 700; font-size: 13px; color: var(--text-gray); margin-top: 1px; }
  .address {
    margin-top: 34px; font-weight: 900; font-size: 17px;
    color: var(--accent-blue); line-height: 1.2;
  }
  .contact-list { list-style: none; margin-top: 6px; }
  .contact-list li {
    display: flex; align-items: center; gap: 12px;
    font-size: 17px; font-weight: 700; color: var(--text-gray); height: 32px;
  }
  .contact-list svg { width: 17px; height: 17px; fill: var(--text-gray); flex: none; }
  .website { margin-top: 4px; font-weight: 900; font-size: 20px; color: var(--text-gray); }
  .website span { color: var(--accent-blue); }
</style>
</head>
<body>
  <section class="card card-back" aria-label="Appointment side">
    <svg class="card-bands" viewBox="0 0 720 412" preserveAspectRatio="none" aria-hidden="true">
      <path fill="var(--sky)" d="M0 0 H720 V8 H0 Z"/>
      <path fill="var(--sky)" d="M0 412 H720 V388 H210 C175 388 170 404 135 404 H0 Z"/>
    </svg>
    <p class="quote">“Physical fitness can neither be achieved by wishful thinking nor outright purchased.”</p>
    <p class="quote-author">— Conrad Vellmer</p>
    <ul class="day-picker">
      <li>Mon <span class="check-box"></span></li>
      <li>Tue <span class="check-box"></span></li>
      <li>Wed <span class="check-box"></span></li>
      <li>Thu <span class="check-box"></span></li>
      <li>Fri <span class="check-box"></span></li>
      <li>Sat <span class="check-box"></span></li>
    </ul>
    <div class="slot-row">
      <span>Date:</span><span class="slot-line"></span>
      <span>Time:</span><span class="slot-line short"></span>
      <span class="meridiem"><span>AM</span><span>PM</span></span>
    </div>
  </section>

  <section class="card card-front" aria-label="Contact side">
    <svg class="card-bands" viewBox="0 0 720 412" preserveAspectRatio="none" aria-hidden="true">
      <path fill="var(--sky)" d="M180 24 C215 24 225 8 260 8 H720 V0 H180 Z"/>
      <path fill="var(--sky)" d="M0 412 H720 V404 H590 C560 404 555 386 520 386 H0 Z"/>
    </svg>
    <div class="brand">
      <span class="brand-dot"></span>
      <span class="brand-name">Orchard Row</span>
    </div>
    <div class="divider"></div>
    <div class="contact">
      <p class="holder-name">YOUR NAME</p>
      <p class="holder-role">Designation</p>
      <p class="address">14 Rue des Vergers,<br>77400 Lagny le Haut</p>
      <ul class="contact-list">
        <li>
          <svg viewBox="0 0 24 24" aria-label="Phone"><path d="M3 8c0-2 3-4 9-4s9 2 9 4v2h-5V8H8v2H3z M5 12h14l2 8H3z"/></svg>
          +33 (0)1 42 55 08 19
        </li>
        <li>
          <svg viewBox="0 0 24 24" aria-label="Mobile"><path d="M7 1h10a2 2 0 0 1 2 2v18a2 2 0 0 1-2 2H7a2 2 0 0 1-2-2V3a2 2 0 0 1 2-2zm0 3v15h10V4z"/></svg>
          +33 (0)6 51 30 74 86
        </li>
        <li>
          <svg viewBox="0 0 24 24" aria-label="Fax"><path d="M6 2h12v6H6z M2 9h20v10h-4v3H6v-3H2z M8 15v5h8v-5z"/></svg>
          +33 (0)1 42 55 08 19
        </li>
        <li>
          <svg viewBox="0 0 24 24" aria-label="Email"><path d="M2 5h20v14H2z M4 7v1l8 5 8-5V7l-8 5z" fill-rule="evenodd"/></svg>
          info@orchardrow.com
        </li>
      </ul>
      <p class="website">www.<span>orchardrow</span>.com</p>
    </div>
  </section>
</body>
</html>
```